****Business Card Design for Cormwell Development. Design based around attached logo/company name

I’m looking for business card design for my company Cormwell Development Group,LLC. Design should be professional, sharp and minimal. Outside of the attached logos, greyscale colors for remainder of cards. My thoughts are two-sided card with attached logo on one side and my info on the other but open to one-sided as well with right design.
Target Market(s)
Real estate professionals including banks, private investors, property owners, developers, commercial tenants like Brewlantic, Granvey or Tamsett’s.
Industry/Entity Type
Commercial real estate development and investments.
Contact Information for Business Card
Name, title, email, phone #’s, web address and physical address
Font styles to use
Other font styles liked:
- Helvetica, Garamond, etc
Colors
Designer to choose only greyscale colors for use in the design.
Requirements
Must have
- Attached logo first or second options.
Nice to have
- Two sided card with logo on one side. Attached Logo/company name can be laid out any way that flows as long as it’s legible.name
Should not have
- No loud colors. ***Please do not include logo, I have removed the company design with a logo image.

```html
<!DOCTYPE html>
<html lang="en">
<head>
<meta charset="utf-8">
<title>Cormwell Development Group, LLC — Business Card</title>
<link rel="stylesheet" href="https://fonts.googleapis.com/css2?family=Roboto:wght@400;500&display=swap">
<style>
  :root {
    --backdrop: #9a9b9a;
    --paper: #ffffff;
    --slate: #5e6577;
    --silver: #8e9190;
    --ink: #5a6070;
    --ink-soft: #6b7080;
    --line: #6b7080;
  }
  * { box-sizing: border-box; margin: 0; padding: 0; }
  html, body {
    width: 1200px; height: 1200px; overflow: hidden;
    background: var(--backdrop);
    font-family: "Roboto", Helvetica, Arial, sans-serif;
  }
  .card {
    position: absolute; left: 232px; width: 736px; height: 450px; overflow: hidden;
  }
  .card--front {
    top: 116px; background: var(--paper);
    border-radius: 0 32px 0 32px;
  }
  .card--back {
    top: 632px; background: var(--slate);
    border-radius: 32px 0 32px 0;
  }
  .front-wave { position: absolute; left: 0; top: 0; width: 736px; height: 450px; }
  .brand-box {
    position: absolute; left: 44px; top: 178px; width: 300px; height: 97px;
    background: var(--slate); color: #eef0f3;
    display: flex; flex-direction: column; justify-content: center; align-items: flex-end;
    padding-right: 22px; font-weight: 400;
  }
  .brand-box .brand-name { font-size: 30px; letter-spacing: 1px; line-height: 1.05; }
  .brand-box .brand-sub { font-size: 12px; letter-spacing: 1.2px; text-transform: uppercase; margin-top: 4px; }
  .divider {
    position: absolute; left: 380px; top: 120px; width: 2px; height: 212px; background: var(--line);
  }
  .person { position: absolute; left: 412px; top: 112px; }
  .person-name { font-size: 30px; font-weight: 400; color: var(--ink); letter-spacing: 0.3px; }
  .person-title { font-size: 22px; color: var(--ink-soft); margin-top: 2px; }
  .contact-list { position: absolute; left: 412px; top: 210px; list-style: none; }
  .contact-list li {
    display: flex; align-items: center; height: 33px;
    font-size: 20px; color: var(--ink);
  }
  .contact-list svg { width: 20px; height: 20px; margin-right: 12px; flex: none; fill: none; stroke: var(--ink); stroke-width: 1.8; }
  .back-brand {
    position: absolute; left: 200px; top: 160px; color: #ffffff; font-weight: 400;
  }
  .back-brand .brand-name { font-size: 62px; letter-spacing: 3px; line-height: 1; }
  .back-brand .brand-sub { font-size: 26px; letter-spacing: 2.5px; text-transform: uppercase; margin-top: 12px; }
</style>
</head>
<body>
  <section class="card card--front">
    <svg class="front-wave" viewBox="0 0 736 450" aria-hidden="true">
      <path d="M0 376 Q 330 440 700 370 Q 400 430 0 400 Z" fill="var(--silver)"/>
      <path d="M0 408 Q 380 450 736 356 L736 450 L0 450 Z" fill="var(--slate)"/>
    </svg>
    <div class="brand-box">
      <span class="brand-name">CORMWELL</span>
      <span class="brand-sub">Development Group, LLC</span>
    </div>
    <div class="divider"></div>
    <div class="person">
      <h1 class="person-name">DORIAN HALVERS</h1>
      <p class="person-title">President</p>
    </div>
    <ul class="contact-list">
      <li>
        <svg viewBox="0 0 20 20"><rect x="5" y="1.5" width="10" height="17" rx="1.5"/><line x1="9" y1="15.5" x2="11" y2="15.5"/></svg>
        012 3456 7890
      </li>
      <li>
        <svg viewBox="0 0 20 20"><path d="M2 7 Q10 1 18 7 L16 9 L13 7.5 L7 7.5 L4 9 Z" fill="var(--ink)"/><rect x="4" y="10" width="12" height="7" rx="2" fill="var(--ink)"/></svg>
        012 3456 7890
      </li>
      <li>
        <svg viewBox="0 0 20 20"><rect x="1.5" y="4" width="15" height="11"/><path d="M1.5 4 L9 10 L16.5 4"/><circle cx="16" cy="15" r="3" fill="var(--ink)" stroke="none"/></svg>
        info@yourmail.com
      </li>
      <li>
        <svg viewBox="0 0 20 20"><circle cx="10" cy="10" r="8"/><ellipse cx="10" cy="10" rx="3.5" ry="8"/><line x1="2" y1="10" x2="18" y2="10"/></svg>
        www.yourwebside.com
      </li>
    </ul>
  </section>

  <section class="card card--back">
    <div class="back-brand">
      <div class="brand-name">CORMWELL</div>
      <div class="brand-sub">Development Group, LLC</div>
    </div>
  </section>
</body>
</html>
```